Business Card Design

We need a new business card design for a CPA office that has been in business for over 10 years. We are a Accounting Concierge firm that offers the following services: Certified Public Accountant, Personal & Business Tax Preparation, Accounting, Bookkeeping, Payroll Services, Tax Litigation Services.
Certified LedgerNest CertPartner.  We would like to see designs that use the color navy blue in the company logo with classic accent colors.  We would like the card to be on a textured high pound card stock and that is more classic and less modern in design.  The final design should communicate class and professionalism.

Reason: I gave feedback to many of the designers with some changes.  Please re-read the brief as we would like to remove the photo of the man on the card.  We also want only light grey or white background, not navy or blue - the navy or blue tones should be the font or accent colors.  Please also, consider creating a logo with the initials P&W or PW or P&W CPA.

Industry/Entity Type
Business
Contact Information for Business Card
Pellford & Company CPA, Dominic Pellford III, 4317 Larkmoor Road, Suite D, Bradenton, FL  34519, Phone: (941) 555-0137, Fax: (941) 555-0182, Email: Dominic@DPellfordCPA.example, Website: www.DPellfordCPA.example
Requirements
Must have
- LedgerNest Logo

Should not have
- we no longer want the photo on the card.

```html
<!DOCTYPE html>
<html lang="en">
<head>
<meta charset="utf-8">
<title>Pellford &amp; Company CPA – Business Card</title>
<link rel="stylesheet" href="https://fonts.googleapis.com/css2?family=Questrial&display=swap">
<style>
  :root {
    --page-bg: #dcdcda;
    --card-paper: #f6f6f4;
    --card-paper-edge: #ececea;
    --ink-navy: #2b3266;
    --ink-navy-soft: #4a5185;
    --rule: #2b3266;
    --badge-gold: #f3b51c;
  }
  * { box-sizing: border-box; margin: 0; padding: 0; }
  html, body {
    width: 1200px; height: 1200px; overflow: hidden;
    background: var(--page-bg);
  }
  .stage {
    width: 1200px; height: 1200px;
    display: flex; align-items: center; justify-content: center;
  }
  .business-card {
    position: relative;
    width: 1050px; height: 600px;
    background: linear-gradient(160deg, var(--card-paper) 0%, var(--card-paper-edge) 100%);
    color: var(--ink-navy);
    font-family: "Questrial", "Century Gothic", sans-serif;
    box-shadow: 0 10px 30px rgba(0,0,0,0.14);
  }
  .firm-name {
    position: absolute; right: 70px; top: 62px;
    font-size: 56px; font-weight: 400; letter-spacing: 0.5px;
    white-space: nowrap;
  }
  .firm-tagline {
    position: absolute; right: 110px; top: 140px;
    font-size: 31px; font-weight: 400; letter-spacing: 0.6px;
    color: var(--ink-navy-soft); white-space: nowrap;
  }
  .double-rule {
    position: absolute; left: 0; right: 0; top: 226px;
    height: 7px;
    border-top: 2px solid var(--rule);
    border-bottom: 2px solid var(--rule);
  }
  .principal {
    position: absolute; left: 60px; top: 292px;
  }
  .principal-name {
    font-size: 42px; font-weight: 400; letter-spacing: 0.4px;
    white-space: nowrap;
  }
  .principal-phone {
    display: flex; align-items: center; gap: 14px;
    margin: 14px 0 0 110px; font-size: 27px; white-space: nowrap;
  }
  .partner-badge {
    position: absolute; left: 142px; top: 425px;
    width: 160px; height: 118px;
  }
  .contact-list {
    position: absolute; left: 520px; top: 270px;
    list-style: none; font-size: 27px; letter-spacing: 0.4px;
  }
  .contact-item {
    display: flex; align-items: flex-start; gap: 20px;
    margin-bottom: 18px; line-height: 1.2; white-space: nowrap;
  }
  .contact-icon {
    flex: 0 0 26px; width: 26px; height: 26px; margin-top: 3px;
  }
</style>
</head>
<body>
<main class="stage">
  <article class="business-card">
    <h1 class="firm-name">Pellford &amp; Company CPA, LLC</h1>
    <p class="firm-tagline">Full Service Tax and Accounting</p>
    <div class="double-rule"></div>

    <section class="principal">
      <h2 class="principal-name">Dominic Pellford</h2>
      <p class="principal-phone">
        <svg class="contact-icon" viewBox="0 0 24 24" aria-hidden="true"><path fill="currentColor" d="M6.6 10.8a15 15 0 0 0 6.6 6.6l2.2-2.2c.3-.3.7-.4 1-.2 1.1.4 2.3.6 3.6.6.6 0 1 .4 1 1V20c0 .6-.4 1-1 1A17 17 0 0 1 3 4c0-.6.4-1 1-1h3.5c.6 0 1 .4 1 1 0 1.3.2 2.5.6 3.6.1.3 0 .7-.2 1z"/></svg>
        (941) 555-0137
      </p>
    </section>

    <svg class="partner-badge" viewBox="0 0 160 118" role="img" aria-label="LedgerNest CertPartner certification badge">
      <ellipse cx="80" cy="59" rx="78" ry="57" fill="var(--badge-gold)"/>
    </svg>

    <ul class="contact-list">
      <li class="contact-item">
        <svg class="contact-icon" viewBox="0 0 24 24" aria-hidden="true"><path fill="currentColor" d="M12 2a7 7 0 0 0-7 7c0 5 7 13 7 13s7-8 7-13a7 7 0 0 0-7-7zm0 9.5A2.5 2.5 0 1 1 12 6.5a2.5 2.5 0 0 1 0 5z"/></svg>
        <span>III, 4317 Larkmoor Road, Suite D,<br>Bradenton, FL 34519</span>
      </li>
      <li class="contact-item">
        <svg class="contact-icon" viewBox="0 0 24 24" aria-hidden="true"><path fill="currentColor" d="M7 3h8l2 2v4H7zM4 10h16a1 1 0 0 1 1 1v7H3v-7a1 1 0 0 1 1-1zm3 4v5h10v-5z"/></svg>
        <span>(941) 555-0182</span>
      </li>
      <li class="contact-item">
        <svg class="contact-icon" viewBox="0 0 24 24" aria-hidden="true"><path fill="none" stroke="currentColor" stroke-width="1.8" d="M3 6h18v12H3zM3 6l9 7 9-7"/></svg>
        <span>dominic@dpellfordcpa.example</span>
      </li>
      <li class="contact-item">
        <svg class="contact-icon" viewBox="0 0 24 24" aria-hidden="true"><g fill="none" stroke="currentColor" stroke-width="1.6"><circle cx="12" cy="12" r="9"/><ellipse cx="12" cy="12" rx="4" ry="9"/><path d="M3 12h18M5 7h14M5 17h14"/></g></svg>
        <span>www.dpellfordcpa.example</span>
      </li>
    </ul>
  </article>
</main>
</body>
</html>
```